Logo and Double sided business card

We need a logo and business card for a Point of Sale Business, Website is www.kestreltill.com.au - this is being worked on at the moment. There is a logo on the website - but this is more of a placement /logo and needs to be redesigned.
The address for Details for the Business card are

Person Name
KESTREL TILL
17/3 Worrigal Pde
Marrowby 2187
Ph 1300 585 926 (1300 KTL 926)
Email : Person@kestreltill.com.au
Web: www.kestreltill.com.au

Our company will be a Point of Sale installation and Support business. We Specialise in the Vandrel Quill system.

We do
Installation of POS Systems
Support and Maintenance of existing POS
Quill POS support
Updates

Target Market(s)

Restaurants, hotels, retail shops

Industry/Entity Type

Business

Contact Information for Business Card

Person Name
KESTREL TILL
17/3 Worrigal Pde
Marrowby 2187
Web: www.kestreltill.com.au

Logo Text

Kestrel Till

Font styles to use
Serif

Requirements
Must have
• We must have the source graphics in editable formats for both logo and business card.

```html
<!DOCTYPE html>
<html lang="en">
<head>
<meta charset="utf-8">
<title>Kestrel Till – Business Card</title>
<link href="https://fonts.googleapis.com/css2?family=Source+Sans+3:wght@400;600;700&display=swap" rel="stylesheet">
<style>
  :root {
    --orange: #f07b12;
    --white: #ffffff;
    --panel: #f6f3f0;
    --backdrop: #e7e3df;
    --ink: #3a3a3a;
    --faint: #f5c9a0;
  }
  * { margin: 0; padding: 0; box-sizing: border-box; }
  html, body { width: 1200px; height: 900px; overflow: hidden; }
  body {
    background: var(--backdrop);
    font-family: "Source Sans 3", "Myriad Pro", Arial, sans-serif;
    position: relative;
  }
  .card {
    position: absolute;
    display: flex;
    box-shadow: 0 6px 18px rgba(0,0,0,0.12);
  }
  .card-front { left: 238px; top: 62px; width: 555px; height: 343px; }
  .card-back { left: 459px; top: 518px; width: 560px; height: 342px; }

  .panel-light {
    background: var(--panel);
    display: flex;
    align-items: center;
    justify-content: center;
  }
  .panel-orange { background: var(--orange); color: var(--white); }

  .card-front .panel-light { width: 255px; }
  .card-front .panel-orange { width: 300px; padding: 66px 0 0 32px; }

  .brand-mark {
    display: flex; align-items: center; gap: 10px;
    font-weight: 700; letter-spacing: 1px; white-space: nowrap;
  }
  .brand-dot { border-radius: 50%; flex: none; }

  .brand-large { color: var(--orange); font-size: 28px; }
  .brand-large .brand-dot { width: 22px; height: 22px; background: var(--ink); }

  .brand-faint { color: var(--faint); font-size: 24px; }
  .brand-faint .brand-dot { width: 18px; height: 18px; background: var(--faint); }

  .person-name { font-size: 20px; font-weight: 700; line-height: 1.1; }
  .person-role { font-size: 16px; line-height: 1.2; }
  .address { font-size: 16px; line-height: 1.3; margin-top: 54px; }
  .contact-list { list-style: none; margin-top: 18px; font-size: 16px; line-height: 1.3; }
  .contact-list li { display: flex; align-items: center; gap: 8px; }
  .contact-list svg { width: 12px; height: 12px; flex: none; }

  .card-back .panel-orange {
    width: 310px;
    display: flex; flex-direction: column; align-items: center;
    padding-top: 82px;
  }
  .card-back .panel-light { width: 250px; }
  .brand-back { color: var(--white); font-size: 34px; }
  .brand-back .brand-dot { width: 26px; height: 26px; background: var(--white); }
  .services {
    list-style: none; text-align: center;
    font-size: 16px; font-weight: 600; line-height: 1.3;
    margin-top: 76px;
  }
</style>
</head>
<body>

  <section class="card card-front" aria-label="Business card front">
    <div class="panel-light">
      <div class="brand-mark brand-large"><span class="brand-dot"></span>Kestrel Till</div>
    </div>
    <div class="panel-orange">
      <p class="person-name">Daniel Marsh</p>
      <p class="person-role">Managing Director</p>
      <p class="address">17/3 Worrigal Pde Marrowby<br>2187</p>
      <ul class="contact-list">
        <li>
          <svg viewBox="0 0 12 12"><path fill="#fff" d="M2.5 1 L4.5 1 L5.3 3.4 L4 4.4 Q5 6.8 7.6 8 L8.6 6.7 L11 7.5 L11 9.5 Q10.5 11 9 11 Q1 10 1 2.8 Q1 1.3 2.5 1Z"/></svg>
          1300 585 926 (1300 KTL 926)
        </li>
        <li>
          <svg viewBox="0 0 12 12"><rect x="1" y="3" width="10" height="7" fill="#fff"/><path d="M1 3 L6 7 L11 3" stroke="#f07b12" fill="none" stroke-width="1"/></svg>
          Person@kestreltill.com.au
        </li>
        <li>
          <svg viewBox="0 0 12 12"><circle cx="6" cy="6" r="5" fill="#fff"/><path d="M1 6 H11 M6 1 Q3 6 6 11 M6 1 Q9 6 6 11" stroke="#f07b12" fill="none" stroke-width="0.9"/></svg>
          www.kestreltill.com.au
        </li>
      </ul>
    </div>
  </section>

  <section class="card card-back" aria-label="Business card back">
    <div class="panel-orange">
      <div class="brand-mark brand-back"><span class="brand-dot"></span>KESTREL TILL</div>
      <ul class="services">
        <li>Installation of POS Systems</li>
        <li>Support and</li>
        <li>Maintenance of existing POS</li>
        <li>Quill POS support</li>
      </ul>
    </div>
    <div class="panel-light">
      <div class="brand-mark brand-faint"><span class="brand-dot"></span>Kestrel Till</div>
    </div>
  </section>

</body>
</html>
```